CD Cover for southern rock band

We need a CD sleve design for our southern rock band named 'Seven Creeks Past Dawson'. We are a southern rock band with some country roots to our music. The name of this CD is 'Rusted & Loud EP'. We would like our design to reflect the country-rock lifestyle but also give it that "RUSTED and loud" feel as our album is titled that. We want a cover that can be appealing for both guys and girls but still have that country ROCK music type of feel. Just some ideas that you could use for the photograph are mud volleyball girls, trucks, lake parties, or country sunset scenes with a couple watching it.

Target Market(s)

Country Music Listeners of ages 18-45

Industry/Entity Type

Music Download

Requirements
Must have
• A countryesque photograph cover that can tell a story when you look at it.
• The song titles in order for the back of the sleeve are as follows:
• 1. Cinder Canyon
• 2. Lady On The Porch
• 3. Turn Away
• 4. Ol' Barnaby
• 5. Turn Away (Acoustic Version)
Nice to have
• The laid back country feel while also conveying a RUSTED and loud feel. The perfect mix of fun YET HARD ASS!
Should not have
• Should not be a super cliche album cover. No human skulls. Not just a plain background.

```html
<!DOCTYPE html>
<html lang="en">
<head>
<meta charset="utf-8">
<title>Rusted &amp; Loud EP — Seven Creeks Past Dawson</title>
<link rel="stylesheet" href="https://fonts.googleapis.com/css2?family=Roboto+Condensed:wght@700&family=Playfair+Display:ital@1&display=swap">
<style>
  :root {
    --frame-white: #ffffff;
    --title-white: #ffffff;
    --band-ink: #1b1b1b;
    --sky-peach: #ecc8a8;
    --sky-rose: #b97f82;
    --sky-teal: #7fdcc8;
    --sky-mint: #b4efdc;
    --haze-blue: #5aa5b0;
    --hill-green: #3f8a45;
    --hill-deep: #2c5e4e;
    --ridge-blue: #2f5f72;
    --river-blue: #3a86a8;
    --rust-glow: #d99a52;
  }
  html, body {
    margin: 0;
    padding: 0;
    width: 1200px;
    height: 1200px;
    overflow: hidden;
    background: #ffffff;
  }
  .cover {
    position: relative;
    width: 1200px;
    height: 1200px;
    overflow: hidden;
  }
  .cover-photo {
    position: absolute;
    inset: 0;
    background:
      radial-gradient(ellipse 9% 6% at 20% 80%, rgba(217,154,82,0.75), rgba(217,154,82,0) 100%),
      radial-gradient(ellipse 38% 26% at 100% 2%, rgba(185,127,130,0.85), rgba(185,127,130,0) 100%),
      radial-gradient(ellipse 45% 16% at 22% 0%, rgba(236,200,168,0.9), rgba(236,200,168,0) 100%),
      radial-gradient(ellipse 16% 30% at 53% 100%, rgba(58,134,168,0.95), rgba(58,134,168,0) 100%),
      radial-gradient(ellipse 12% 5% at 52% 62%, rgba(120,200,210,0.8), rgba(120,200,210,0) 100%),
      radial-gradient(ellipse 42% 38% at 10% 88%, rgba(63,138,69,0.95), rgba(63,138,69,0) 100%),
      radial-gradient(ellipse 40% 36% at 96% 84%, rgba(44,94,78,0.95), rgba(44,94,78,0) 100%),
      radial-gradient(ellipse 40% 14% at 78% 56%, rgba(47,95,114,0.8), rgba(47,95,114,0) 100%),
      radial-gradient(ellipse 55% 25% at 45% 28%, rgba(180,239,220,0.8), rgba(180,239,220,0) 100%),
      linear-gradient(180deg,
        var(--sky-peach) 0%,
        #9fd9c6 10%,
        var(--sky-teal) 22%,
        var(--sky-mint) 36%,
        #8fe0c9 46%,
        var(--haze-blue) 54%,
        #3c7f6e 66%,
        var(--hill-deep) 82%,
        var(--ridge-blue) 100%);
  }
  .frame {
    position: absolute;
    border: 10px solid var(--frame-white);
    box-sizing: border-box;
  }
  .frame--back  { left: 101px; top: 57px;  width: 1042px; height: 1042px; }
  .frame--front { left: 57px;  top: 108px; width: 1040px; height: 1041px; }
  .title {
    position: absolute;
    right: 291px;
    top: 418px;
    margin: 0;
    font-family: "Roboto Condensed", "Arial Narrow", sans-serif;
    font-weight: 700;
    font-size: 160px;
    line-height: 138px;
    letter-spacing: -2px;
    color: var(--title-white);
    text-align: right;
    text-transform: uppercase;
  }
  .title span { display: block; }
  .edition {
    position: absolute;
    right: 291px;
    top: 704px;
    margin: 0;
    font-family: "Playfair Display", Georgia, serif;
    font-style: italic;
    font-size: 66px;
    line-height: 1;
    color: var(--title-white);
  }
  .band-name {
    position: absolute;
    right: 274px;
    top: 780px;
    margin: 0;
    font-family: "Roboto Condensed", "Arial Narrow", sans-serif;
    font-weight: 700;
    font-size: 74px;
    line-height: 100px;
    color: var(--band-ink);
    text-align: right;
    text-transform: uppercase;
  }
  .band-name span { display: block; }
</style>
</head>
<body>
  <main class="cover">
    <div class="cover-photo" role="img" aria-label="Aerial photograph of a winding river between green forested mountains, sunlit rusty rock patches on the left slope, under a hazy teal sky with warm peach and rose light at the top"></div>
    <div class="frame frame--back"></div>
    <div class="frame frame--front"></div>
    <h1 class="title"><span>Rusted&amp;</span><span>Loud</span></h1>
    <p class="edition">EP</p>
    <p class="band-name"><span>Seven Creeks</span><span>Past Dawson</span></p>
  </main>
</body>
</html>
```